Business Card Design for Bright Harbor Paths, LLC

Using my logo created by Pixel Tide, please create a 2 sided business card that will have an lasting affect on my potential clients. I would like my name (Dennis R. Holt, MBA), title (Owner), phone numbers or Contact Info: 312 555-0148 and 312 555-0193. Website: http://www.brantleyfordcircle.com/dennisholt/. On the back side of the card use the Certified Brantley Ford Seal that I attached. You can decide to put either my company name or what I do or nothing at all.

Target Market(s)

Large to small business, owners, Information Technology Leaders, Government and City Leaders.

Industry/Entity Type

Business

Contact Information for Business Card

It is in the description. I would like my name (Dennis R. Holt, MBA), title (Owner), phone numbers or Contact Info: 312 555-0148 and 312 555-0193. Website: http://www.brantleyfordcircle.com/dennisholt/. On the back side of the card use the Certified Brantley Ford Seal that I attached.

Colors

Designer to choose colors to be used in the design.

Requirements
Must have
• Do not change the seal that is on the back or it's color.

```html
<!DOCTYPE html>
<html lang="en">
<head>
<meta charset="utf-8">
<title>Bright Harbor Paths, LLC — Business Card</title>
<link href="https://fonts.googleapis.com/css2?family=Cinzel:wght@600&family=Lato:wght@300;400&display=swap" rel="stylesheet">
<style>
  :root {
    --maroon: #3d0b10;
    --maroon-deep: #330709;
    --paper: #f7f7f5;
    --ink-light: #e9dcdc;
    --ink-soft: #c9b3b4;
    --seal-gold: #d8a415;
    --seal-rim: #9c7408;
    --backdrop: #ececec;
  }
  * { box-sizing: border-box; margin: 0; padding: 0; }
  html, body { width: 1200px; height: 784px; overflow: hidden; }
  body {
    background: var(--backdrop);
    display: flex; align-items: center; justify-content: center; gap: 60px;
    font-family: "Lato", sans-serif;
  }
  .card {
    width: 520px; height: 297px; position: relative; overflow: hidden;
    box-shadow: 0 6px 18px rgba(0,0,0,.12);
  }
  .card--front { background: var(--paper); }
  .brand {
    position: absolute; top: 52px; left: 0; right: 0;
    display: flex; flex-direction: column; align-items: center;
  }
  .brand__row { display: flex; align-items: center; gap: 10px; }
  .brand__dot { width: 14px; height: 14px; border-radius: 50%; background: var(--maroon); }
  .brand__name {
    font-family: "Cinzel", serif; font-weight: 600; font-size: 24px;
    color: var(--maroon); letter-spacing: .5px;
  }
  .brand__tagline {
    margin-top: 6px; font-family: "Cinzel", serif; font-weight: 600;
    font-size: 11px; letter-spacing: 3px; color: var(--maroon);
  }
  .contact-band {
    position: absolute; left: 0; right: 0; bottom: 0; height: 122px;
    background: var(--maroon);
    display: flex; align-items: center;
  }
  .holder { width: 230px; text-align: right; padding-right: 22px; }
  .holder__name { font-size: 18px; font-weight: 300; color: var(--ink-light); letter-spacing: .3px; }
  .holder__title { font-size: 10px; color: var(--ink-soft); letter-spacing: 1.5px; margin-top: 4px; }
  .divider { width: 1px; height: 66px; background: var(--ink-soft); opacity: .6; }
  .contact { list-style: none; padding-left: 20px; }
  .contact li {
    display: flex; align-items: center; gap: 10px;
    font-size: 12px; color: var(--ink-light); line-height: 21px; letter-spacing: .3px;
  }
  .contact svg { width: 11px; height: 11px; fill: none; stroke: var(--ink-light); stroke-width: 1.6; }
  .card--back { background: var(--maroon-deep); }
  .back-mark {
    position: absolute; top: 96px; left: 0; right: 0; text-align: center;
    font-family: "Cinzel", serif; font-weight: 600; font-size: 24px;
    color: #4a1116;
  }
  .seal {
    position: absolute; left: 50%; top: 168px; transform: translateX(-50%);
    width: 64px; height: 64px; border-radius: 50%;
    background: var(--seal-gold); border: 3px solid var(--seal-rim);
  }
</style>
</head>
<body>
  <section class="card card--front" aria-label="Business card front">
    <div class="brand">
      <div class="brand__row">
        <span class="brand__dot"></span>
        <span class="brand__name">Bright Harbor Paths, LLC</span>
      </div>
      <div class="brand__tagline">SPEAKER, COACH, TRAINER</div>
    </div>
    <div class="contact-band">
      <div class="holder">
        <div class="holder__name">Dennis R. Holt, MBA</div>
        <div class="holder__title">OWNER</div>
      </div>
      <div class="divider"></div>
      <ul class="contact">
        <li><svg viewBox="0 0 12 12"><rect x="3" y="1" width="6" height="10" rx="1"/></svg>312 555-0148</li>
        <li><svg viewBox="0 0 12 12"><path d="M2 3c0 4 3 7 7 7l1-2-2-1-1 1C5 7 5 7 5 5l1-1-1-2z"/></svg>312 555-0193</li>
        <li><svg viewBox="0 0 12 12"><circle cx="6" cy="6" r="5"/><path d="M1 6h10M6 1c-3 3-3 7 0 10M6 1c3 3 3 7 0 10"/></svg>brantleyfordcircle.com/dennisholt</li>
      </ul>
    </div>
  </section>

  <section class="card card--back" aria-label="Business card back">
    <div class="back-mark">Bright Harbor Paths, LLC</div>
    <div class="seal" role="img" aria-label="Certified Brantley Ford member seal"></div>
  </section>
</body>
</html>
```